Consulting company with focus on aviation needs

We need a new business card design for our company. The company consults with multiple players in the industry like manufacturers and airlines. It is also a supplier and an inter-company level. Given the targeted industry (aviation) it should be both kind of serious, sound, secure, classy, ​​but also a bit technical, innovative. Should not be too playful, however, "fresh", "airy", "ligth" and "suprising" are suitabe attributes. The existing logo shall be used.

Industry/Entity Type

Airlines

```html
<!DOCTYPE html>
<html lang="en">
<head>
<meta charset="utf-8">
<title>Velora business card</title>
<link href="https://fonts.googleapis.com/css2?family=Lato:ital,wght@0,400;0,700;1,400;1,700&display=swap" rel="stylesheet">
<style>
  :root {
    --stage: #3a3a3a;
    --teal: #23a083;
    --lime: #9fbb4a;
    --orange: #f39c1f;
    --stone: #7d7d78;
    --ink: #1e1e1e;
    --paper: #ffffff;
  }
  * { margin: 0; padding: 0; box-sizing: border-box; }
  html, body { width: 1200px; height: 900px; overflow: hidden; }
  body {
    background: var(--stage);
    font-family: "Lato", Arial, sans-serif;
    position: relative;
  }
  .card {
    position: absolute;
    width: 760px;
    height: 410px;
    overflow: hidden;
  }
  /* back side */
  .card-back {
    left: 400px; top: 30px;
    background: var(--teal);
    color: var(--paper);
  }
  .back-brand {
    position: absolute;
    left: 0; right: 0; top: 118px;
    text-align: center;
  }
  .brand-row { display: inline-flex; align-items: center; gap: 18px; }
  .brand-dot { width: 34px; height: 34px; border-radius: 50%; background: var(--paper); }
  .brand-name {
    font-weight: 700;
    font-size: 72px;
    letter-spacing: 14px;
    line-height: 1;
  }
  .back-tagline {
    margin-top: 14px;
    color: var(--orange);
    font-size: 22px;
    font-style: italic;
    letter-spacing: 1px;
  }
  .back-web {
    margin-top: 26px;
    font-size: 18px;
    letter-spacing: 1px;
  }
  /* front side */
  .card-front {
    left: 40px; top: 460px;
    background: var(--paper);
    color: var(--ink);
  }
  .front-brand {
    position: absolute;
    left: 50px; top: 140px;
    width: 310px;
  }
  .front-brand .brand-row { gap: 12px; }
  .front-brand .brand-dot { width: 22px; height: 22px; background: var(--teal); }
  .front-brand .brand-name {
    font-size: 50px;
    letter-spacing: 8px;
    color: var(--stone);
  }
  .front-tagline {
    margin-top: 10px;
    color: var(--orange);
    font-size: 15px;
    font-style: italic;
  }
  .divider {
    position: absolute;
    left: 380px; top: 70px;
    width: 2px; height: 230px;
    background: var(--teal);
  }
  .contact {
    position: absolute;
    left: 420px; top: 68px;
  }
  .person-name {
    color: var(--teal);
    font-size: 30px;
    font-weight: 700;
    font-style: italic;
  }
  .person-role { font-size: 18px; margin-top: 2px; }
  .address { font-size: 19px; margin-top: 18px; line-height: 1.3; }
  .lines { list-style: none; margin-top: 12px; font-size: 19px; }
  .lines li { display: flex; align-items: center; gap: 12px; line-height: 1.35; }
  .lines svg { width: 16px; height: 16px; fill: var(--teal); flex: none; }
  .lines .icon-web { fill: none; stroke: var(--teal); stroke-width: 1.6; }
  .color-band {
    position: absolute;
    left: 0; right: 0; bottom: 0;
    height: 12px;
    display: flex;
  }
  .color-band span { flex: 1; }
  .band-teal { background: var(--teal); }
  .band-lime { background: var(--lime); }
  .band-orange { background: var(--orange); }
  .band-stone { background: var(--stone); }
</style>
</head>
<body>

<section class="card card-back">
  <div class="back-brand">
    <div class="brand-row">
      <span class="brand-dot"></span>
      <span class="brand-name">VELORA</span>
    </div>
    <p class="back-tagline">Linking Partners - Shaping Flight</p>
    <p class="back-web">www.velora-air.com</p>
  </div>
</section>

<section class="card card-front">
  <div class="front-brand">
    <div class="brand-row">
      <span class="brand-dot"></span>
      <span class="brand-name">VELORA</span>
    </div>
    <p class="front-tagline">Linking Partners - Shaping Flight</p>
  </div>

  <div class="divider"></div>

  <div class="contact">
    <p class="person-name">Daniel Hartley</p>
    <p class="person-role">Manager</p>
    <p class="address">418 Cedar Lane<br>Houston, TX 77041</p>
    <ul class="lines">
      <li>
        <svg viewBox="0 0 16 16" aria-hidden="true"><path d="M3.6 1.5l2.3 2.6-1.2 1.8c.9 2 2.5 3.6 4.5 4.5l1.8-1.2 2.6 2.3-1.3 2.5C6.8 13.8 2.2 9.2 1.1 2.8z"/></svg>
        512 555 0140
      </li>
      <li>
        <svg viewBox="0 0 16 16" aria-hidden="true"><path d="M4 1h6l2 2v3H4zM2 6h12a1 1 0 011 1v5h-3v3H4v-3H1V7a1 1 0 011-1zm3 5v3h6v-3z"/></svg>
        512 555 0141
      </li>
      <li>
        <svg viewBox="0 0 16 16" aria-hidden="true"><path d="M1 3h14v10H1zm1.5 1.2L8 8.6l5.5-4.4z"/></svg>
        info@velora-air.com
      </li>
      <li>
        <svg class="icon-web" viewBox="0 0 16 16" aria-hidden="true"><circle cx="8" cy="8" r="6.5"/><ellipse cx="8" cy="8" rx="2.8" ry="6.5"/><path d="M1.5 8h13M2.6 4.8h10.8M2.6 11.2h10.8"/></svg>
        www.velora-air.com
      </li>
    </ul>
  </div>

  <div class="color-band">
    <span class="band-teal"></span>
    <span class="band-lime"></span>
    <span class="band-orange"></span>
    <span class="band-stone"></span>
  </div>
</section>

</body>
</html>
```